Letterhead PT. Kencana Tirta Mandiri Developer

Alo , My Company need a letterhead design for PT. Kencana Tirta Mandiri developer Real Estate , i need your each other creative design letterhead for my PT.Kencana Tirta Mandiri Developer Real Estate guys
input my data in letterhead :
Address : Komp. Ruko Seroja Blok F No. 27
No. Telp : 0778 352 6147 / 0812 4539 1768
Email : kencanatirtamandiri@mailbox.example
Website : www.kencanatirtamandiri.example

Target Market(s)

Buyer Property Real Estate & Investor

Industry/Entity Type

Real Estate Development

Font styles to use
Serif
Sans Serif

Requirements
Must have
• according to your creative each other guys as long i need
• Address : Komp. Ruko Seroja Blok F No. 27
• No. Telp : 0778 352 6147 / 0812 4539 1768
• Email : kencanatirtamandiri@mailbox.example
• Website : www.kencanatirtamandiri.example
Nice to have
Should not have
• don't want another colour except : white , dark blue n gold suit to our logo developer real estate

```html
<!DOCTYPE html>
<html lang="en">
<head>
<meta charset="utf-8">
<title>Letterhead – PT. Kencana Tirta Mandiri Developer</title>
<link href="https://fonts.googleapis.com/css2?family=Open+Sans:wght@400;600;700&family=Nunito:wght@400;600&display=swap" rel="stylesheet">
<style>
  :root {
    --navy: #0f3a66;
    --gold: #d0a146;
    --ink: #2a2a2a;
    --muted: #555b63;
    --paper: #ffffff;
    --backdrop: #e6e6e6;
  }
  * { box-sizing: border-box; margin: 0; padding: 0; }
  html, body {
    width: 1200px; height: 1200px; overflow: hidden;
    background: var(--backdrop);
    font-family: "Open Sans", Arial, sans-serif;
  }
  .letterhead {
    position: absolute; left: 211px; top: 50px;
    width: 778px; height: 1100px;
    background: var(--paper);
    box-shadow: 0 4px 18px rgba(0,0,0,.12);
    color: var(--ink);
  }
  .brand {
    position: absolute; left: 64px; top: 78px;
    font-family: "Open Sans", Arial, sans-serif;
    font-weight: 700; font-size: 17px; letter-spacing: .5px;
    color: var(--navy); line-height: 1.25; width: 230px;
  }
  .contact {
    position: absolute; left: 498px; top: 58px;
    border-left: 1.5px solid var(--navy);
    padding: 2px 0 2px 12px;
    font-size: 9px; line-height: 1.55; color: var(--muted);
  }
  .contact li { list-style: none; display: flex; align-items: center; gap: 5px; }
  .contact svg { width: 8px; height: 8px; fill: var(--navy); flex: none; }
  .salutation {
    position: absolute; left: 64px; top: 250px;
    font-size: 13px; font-weight: 600; color: var(--ink);
  }
  .body-copy {
    position: absolute; left: 64px; top: 290px; width: 620px;
    font-size: 12px; line-height: 1.78; color: var(--muted);
  }
  .body-copy p + p { margin-top: 20px; }
  .signature-mark {
    position: absolute; left: 64px; top: 640px;
    width: 90px; height: 46px; background: #eef0f3; border-radius: 4px;
  }
  .signatory { position: absolute; left: 64px; top: 700px; font-family: "Nunito", sans-serif; }
  .signatory .name { font-size: 19px; font-weight: 600; color: var(--ink); }
  .signatory .role { font-size: 13px; color: var(--muted); margin-top: 2px; }
  .footer-band {
    position: absolute; left: 0; bottom: 0; width: 100%; height: 12px;
    display: flex;
  }
  .footer-band .navy { flex: 0 0 66%; background: var(--navy); }
  .footer-band .gold { flex: 1; background: var(--gold); }
</style>
</head>
<body>
<main class="letterhead">
  <header>
    <div class="brand">PT. KENCANA TIRTA MANDIRI DEVELOPER</div>
    <ul class="contact">
      <li>Komp. Ruko Seroja</li>
      <li>Blok F No. 27</li>
      <li><svg viewBox="0 0 10 10"><path d="M2 0.5 L4 2.5 L3 4 C3.7 5.4 4.6 6.3 6 7 L7.5 6 L9.5 8 L8 9.5 C4 9 1 6 0.5 2 Z"/></svg>0778 352 6147</li>
      <li><svg viewBox="0 0 10 10"><path d="M2 0.5 L4 2.5 L3 4 C3.7 5.4 4.6 6.3 6 7 L7.5 6 L9.5 8 L8 9.5 C4 9 1 6 0.5 2 Z"/></svg>0812 4539 1768</li>
      <li><svg viewBox="0 0 10 10"><path d="M0.5 2 H9.5 V8 H0.5 Z M1 2.4 L5 5.4 L9 2.4" /></svg>kencanatirtamandiri@mailbox.example</li>
      <li><svg viewBox="0 0 10 10"><circle cx="5" cy="5" r="4.5"/></svg>www.kencanatirtamandiri.example</li>
    </ul>
  </header>

  <p class="salutation">Dear Mr. Smith,</p>

  <section class="body-copy">
    <p>Lorem ipsum dolor sit amet, consectetur adipiscing elit. Donec orci purus, luctus vitae dignissim eu, iaculis sed purus. Vivamus faucibus, ipsum nec aliquet viverra, leo mauris condimentum ligula, sit amet sagittis enim ligula quis arcu. Nam egestas tortor id nisi porttitor mattis. In tortor ante, ultricies in suscipit a, tempus non massa. Vivamus et auctor mi. Fusce vel massa nulla. Phasellus nec eros mauris, et scelerisque orci. Donec malesuada orci vitae nulla accumsan porta a id massa. Quisque accumsan iaculis magna sit amet fringilla. Maecenas consequat, magna eget tincidunt semper, odio nibh rutrum mi, id feugiat ante nisi eu risus. Vestibulum nunc orci, rhoncus a placerat in, ultricies in mi. Cras mattis varius eros, vel fringilla nisi suscipit eget.</p>
    <p>Quisque scelerisque sagittis nulla at porttitor. Mauris a justo et tellus interdum tristique. Sed id augue vitae urna euismod commodo aliquet a quam. Pellentesque arcu velit, cursus et malesuada ut, consequat et diam. Nullam erat sem, rhoncus id ullamcorper vitae, rhoncus et arcu. In ultricies ultricies nulla, ut rutrum nisi iaculis at. Donec eu magna a metus ornare faucibus. Fusce aliquet faucibus ultricies. Morbi semper, est id tincidunt gravida, sem arcu adipiscing lacus, ac bibendum nulla leo eu purus. Quisque nec diam sed risus consectetur accumsan quis quis nibh. Vestibulum id purus lorem.</p>
  </section>

  <div class="signature-mark" role="img" aria-label="Handwritten signature of John Doe"></div>
  <div class="signatory">
    <p class="name">John Doe</p>
    <p class="role">Co-Founder &amp; CEO</p>
  </div>

  <footer class="footer-band">
    <span class="navy"></span><span class="gold"></span>
  </footer>
</main>
</body>
</html>
```